Luggage and travel essentials company needs Letterhead design (including logo)

Brambury luggage is a travel retailer focussed on selling luggage and travel essentials.
We are a company that have a traditional approach to customer service and also embraces the latest technology, especially where it improves the customer experience.
I would like the design to have an airport hint (airport imagery and font preferred), I would also like the colour blue to feature heavily (see attached image for colour hint).
The final design should aim to give the customer confidence that we are dependable and reliable (no script fonts or crazy colours please) but also reflect that we are an innovative and technology focused company.
I would like the letterhead design to include a logo and text.
I am interested in letterhead text containing an embedded logo (much like the 'Z' in Zephyra's logo is also used separately) Note: this is optional.
The text of the letterhead should include the words "Brambury Luggage & Travel Essentials", and should include a space for the company phone number, email address, website address along with the company physical address.
Target Market(s)
Affluent Adults aged 25 years and above - Predominantly female
Industry/Entity Type
Airport

```html
<!DOCTYPE html>
<html lang="en">
<head>
<meta charset="utf-8">
<title>Brambury Luggage &amp; Travel Essentials – Letterhead</title>
<link href="https://fonts.googleapis.com/css2?family=Exo+2:wght@400;500&display=swap" rel="stylesheet">
<style>
  :root {
    --backdrop: #0b3345;
    --paper: #ffffff;
    --brand-blue: #23a9e1;
    --ink: #3a3a3a;
    --footer-ink: #444444;
  }
  html, body {
    margin: 0;
    padding: 0;
    width: 1200px;
    height: 1000px;
    overflow: hidden;
    background: var(--backdrop);
    font-family: "Exo 2", sans-serif;
  }
  .letterhead {
    position: absolute;
    left: 272px;
    top: 38px;
    width: 656px;
    height: 925px;
    overflow: hidden;
    background: var(--paper);
    box-shadow: 0 6px 24px rgba(0, 0, 0, 0.35);
  }
  .brand {
    position: absolute;
    left: 27px;
    top: 40px;
    display: flex;
    align-items: flex-start;
    color: var(--ink);
  }
  .brand-mark {
    width: 34px;
    height: 34px;
    margin-top: 1px;
    margin-right: 5px;
    background: var(--brand-blue);
    border-radius: 6px;
  }
  .brand-name {
    display: block;
    font-size: 31px;
    font-weight: 500;
    line-height: 34px;
    letter-spacing: -0.6px;
    white-space: nowrap;
  }
  .brand-tagline {
    display: block;
    font-size: 16px;
    font-weight: 500;
    line-height: 16px;
    margin-left: 1px;
    white-space: nowrap;
  }
  .web-band {
    position: absolute;
    left: 397px;
    top: 35px;
    width: 259px;
    height: 60px;
    background: var(--brand-blue);
    color: #ffffff;
    font-size: 14px;
    line-height: 60px;
    padding-left: 56px;
    box-sizing: border-box;
    white-space: nowrap;
    overflow: hidden;
  }
  .contact-footer {
    position: absolute;
    left: 0;
    right: 0;
    bottom: 20px;
    text-align: center;
    color: var(--footer-ink);
    font-size: 10.5px;
    line-height: 17px;
    white-space: nowrap;
  }
  .contact-footer .sep {
    margin: 0 7px;
  }
</style>
</head>
<body>
  <main class="letterhead">
    <header>
      <div class="brand">
        <span class="brand-mark" aria-hidden="true"></span>
        <div>
          <span class="brand-name">Brambury Luggage</span>
          <span class="brand-tagline">&amp; Travel Essentials</span>
        </div>
      </div>
      <div class="web-band">www.bramburyluggage.co.uk</div>
    </header>
    <footer class="contact-footer">
      <div class="address">48, Market Row, Elmsfield, Surrey. RH9 4QT</div>
      <div class="contacts">tel.: 01632 xxxxxx<span class="sep">|</span>info@bramburyluggage.co.uk<span class="sep">|</span>www.bramburyluggage.co.uk</div>
    </footer>
  </main>
</body>
</html>
```